Website design for a personal and professional coaching firm

We need a website design of at least 5 pages for a personal and professional life and leadership Coaching and Life Services Firm. Main Interest: life, relationships and career.
Family, personal development, professional development. Companies and corporations
CHK OUT FRIENDWALL PAGE: OREMBY PATH HOUSE Coaching and Life Services
Target Market(s)
Our Target Audience:
25 to 55 year old men and women living in city, suburbs, and some rural areas. Income from 50k and above. Young professionals, middle of career, college degree. Company, corporate, government, human resources sensitive industries.
Industry/Entity Type
Life Coaching
Number of Pages Required
5+ page
Requirements
Must have
- #1 - relevance/in touch
- #2 - creativity
- #3 - connection with them
Should not have
- the least amount of scrolling the better. Simple, clean and user friendly website not loaded down with a ton of reading

```html
<!DOCTYPE html>
<html lang="en">
<head>
<meta charset="utf-8">
<title>Oremby Path House – Coaching and Life Services</title>
<link rel="stylesheet" href="https://fonts.googleapis.com/css2?family=Jost:wght@400;500&family=Open+Sans:wght@400;600;700&display=swap">
<style>
:root{
  --blue:#0d4ea6;
  --blue-dark:#0a4596;
  --sky:#1f9ad6;
  --yellow:#fbe08a;
  --yellow-strong:#f8d24a;
  --grey:#f2f2f2;
  --text:#444;
  --muted:#777;
  --white:#fff;
}
*{box-sizing:border-box;margin:0;padding:0}
html,body{width:1200px;height:3321px;overflow:hidden}
body{position:relative;font-family:"Open Sans",Arial,sans-serif;color:var(--text);background:var(--white)}
.abs{position:absolute}
.heading{font-family:"Jost",Arial,sans-serif;font-weight:400;color:var(--blue)}
.btn{position:absolute;display:flex;align-items:center;justify-content:center;font-family:"Open Sans",Arial,sans-serif;font-weight:700;font-size:12px;letter-spacing:.5px;text-transform:uppercase}
.btn-blue{background:var(--blue);color:var(--white)}
.btn-yellow{background:var(--yellow);color:var(--blue)}

/* header */
.site-header{position:absolute;left:0;top:0;width:1200px;height:130px;background:var(--white)}
.brand{position:absolute;left:132px;top:30px;display:flex;align-items:center;gap:14px}
.brand-dot{width:44px;height:44px;border-radius:50%;background:var(--blue)}
.brand-name{font-family:"Jost",Arial,sans-serif;font-weight:500;font-size:30px;line-height:1.05;color:var(--blue);letter-spacing:1px}
.header-phone{position:absolute;top:24px}
.header-phone small{display:block;font-size:11px;color:var(--muted);margin-bottom:3px}
.header-phone b{font-family:"Jost",Arial,sans-serif;font-weight:500;font-size:19px;color:var(--blue)}
.phone-badge{position:absolute;left:575px;top:28px;width:36px;height:36px;border-radius:50%;background:var(--yellow);display:flex;align-items:center;justify-content:center}
.main-nav{position:absolute;top:90px;left:582px;display:flex;gap:0;font-size:12px;text-transform:uppercase}
.main-nav a{display:block;padding:5px 10px;color:#555;text-decoration:none}
.main-nav a.active{background:var(--blue);color:var(--white)}

/* hero */
.hero{position:absolute;left:0;top:130px;width:1200px;height:502px;background:linear-gradient(100deg,#a9c9dc 0%,#cfe0ea 35%,#efe8d2 70%,#f6edc9 100%)}
.hero-title{position:absolute;left:130px;top:130px;font-size:54px}
.hero-copy{position:absolute;left:132px;top:212px;width:440px;font-size:16px;line-height:28px;color:#444}
.slider-arrow{position:absolute;width:46px;height:50px;background:rgba(120,120,120,.75);display:flex;align-items:center;justify-content:center}

/* intro */
.intro{position:absolute;left:0;top:632px;width:1200px;height:228px;border-top:3px solid var(--blue)}
.intro-rule{position:absolute;top:0;width:1px;height:228px;background:#e6e6e6}
.intro-icon{position:absolute;top:-50px;width:100px;height:100px;border-radius:50%;border:5px solid var(--white);display:flex;align-items:center;justify-content:center;box-shadow:0 0 0 1px #e3e3e3}
.intro-text{position:absolute;top:86px;width:280px;text-align:center;font-size:16px;line-height:28px;color:#444}

/* about */
.about{position:absolute;left:0;top:860px;width:1200px;height:610px;background:var(--grey)}
.section-title{font-size:34px;text-transform:uppercase}
.about-card{position:absolute;left:135px;top:130px;width:565px;height:412px;background:var(--white)}
.about-card p{position:absolute;left:52px;width:405px;font-size:12.5px;line-height:24px;color:#666;text-align:justify}
.about-photo{position:absolute;left:645px;top:152px;width:423px;height:360px;border:6px solid var(--yellow);background:linear-gradient(180deg,#ece9ec,#c9c3c6)}

/* services */
.services{position:absolute;left:0;top:1470px;width:1200px;height:580px;background:var(--white)}
.title-rule{position:absolute;left:555px;top:128px;width:90px;height:3px;background:var(--yellow)}
.service-card{position:absolute;top:202px;width:295px;height:277px;border:6px solid}
.service-card .photo{position:absolute;inset:0}
.service-card h3{position:absolute;left:20px;top:186px;color:var(--white);font-size:17px;line-height:21px;font-weight:700;text-transform:uppercase}

/* video */
.video{position:absolute;left:0;top:2050px;width:1200px;height:490px;background:var(--grey)}
.video-panel{position:absolute;left:133px;top:48px;width:253px;height:384px;background:var(--blue)}
.video-panel h2{position:absolute;left:44px;top:42px;font-family:"Jost",Arial,sans-serif;font-weight:500;font-size:29px;color:var(--yellow-strong);text-transform:uppercase}
.video-panel p{position:absolute;left:44px;top:110px;font-family:"Jost",Arial,sans-serif;font-size:29px;line-height:42px;color:var(--white);text-transform:uppercase}
.video-frame{position:absolute;left:386px;top:48px;width:680px;height:384px;background:linear-gradient(160deg,#6f9a4a 0%,#4b7a30 45%,#8da769 100%)}
.video-caption{position:absolute;left:68px;top:305px;font-weight:700;font-size:27px;color:var(--white)}
.video-bar{position:absolute;left:0;bottom:0;width:680px;height:46px;background:linear-gradient(0deg,rgba(0,0,0,.45),rgba(0,0,0,0))}

/* call */
.call-title{position:absolute;left:0;top:2620px;width:1200px;text-align:center;font-size:33px}
.contact-strip{position:absolute;left:133px;top:2725px;width:935px;height:118px;border:1px solid #e3e3e3;background:var(--white)}
.contact-item{position:absolute;top:30px}
.contact-item small{display:block;font-family:"Jost",Arial,sans-serif;font-size:17px;color:#555;text-transform:uppercase;margin-bottom:4px}
.contact-item b{font-family:"Jost",Arial,sans-serif;font-weight:500;font-size:21px;color:var(--blue)}
.contact-badge{position:absolute;top:35px;width:44px;height:44px;border-radius:50%;background:var(--yellow);display:flex;align-items:center;justify-content:center}
.contact-rule{position:absolute;top:22px;width:1px;height:74px;background:#ddd}

/* footer */
.site-footer{position:absolute;left:0;top:2918px;width:1200px;height:403px;background:var(--blue);border-top:6px solid var(--yellow)}
.footer-brand{position:absolute;left:132px;top:80px;display:flex;align-items:center;gap:14px}
.footer-brand .brand-dot{background:var(--white)}
.footer-brand .brand-name{color:var(--white)}
.footer-col{position:absolute;top:70px;color:var(--white)}
.footer-col h4{font-size:12px;font-weight:700;text-transform:uppercase;margin-bottom:20px}
.footer-col li{list-style:none;font-size:11px;line-height:24px;color:#cfe0f5}
.social{display:flex;align-items:center;gap:16px;font-size:11px;color:#dfe9f7;margin-bottom:18px}
.social span.dot{width:32px;height:32px;border-radius:50%}
.newsletter-field{width:250px;height:44px;background:#2a67b8;display:flex;align-items:center;padding-left:18px;gap:12px;font-size:11px;color:#c7d7ee}
.footer-rule{position:absolute;left:133px;top:310px;width:935px;height:1px;background:#3a6fbb}
.copyright{position:absolute;left:0;top:348px;width:1200px;text-align:center;font-size:11px;color:#d7e3f4}
</style>
</head>
<body>

<header class="site-header">
  <div class="brand"><span class="brand-dot"></span><span class="brand-name">OREMBY<br>PATH HOUSE</span></div>
  <div class="phone-badge"><svg width="18" height="18" viewBox="0 0 24 24"><path d="M6.6 10.8a15 15 0 0 0 6.6 6.6l2.2-2.2c.3-.3.7-.4 1-.2 1.1.4 2.3.6 3.6.6.6 0 1 .4 1 1V20c0 .6-.4 1-1 1A17 17 0 0 1 3 4c0-.6.4-1 1-1h3.5c.6 0 1 .4 1 1 0 1.3.2 2.5.6 3.6.1.3 0 .7-.2 1z" fill="#0d4ea6"/></svg></div>
  <div class="header-phone" style="left:636px"><small>Ashgrove</small><b>555-014-2200</b></div>
  <div class="header-phone" style="left:796px"><small>Kellan</small><b>555-016-4636</b></div>
  <div class="header-phone" style="left:960px"><small>Fairmoor</small><b>555-018-4636</b></div>
  <nav class="main-nav">
    <a class="active" href="#">Home</a>
    <a href="#" style="margin-left:28px">About us</a>
    <a href="#" style="margin-left:36px">Services</a>
    <a href="#" style="margin-left:46px">Blog</a>
    <a href="#" style="margin-left:52px">Contact us</a>
  </nav>
</header>

<section class="hero" role="img" aria-label="Smiling couple in sunglasses embracing outdoors under a bright sky">
  <h1 class="hero-title heading">Relationships</h1>
  <p class="hero-copy">The Oremby Path House provides coaching centered on your career, leadership, organization or business.</p>
  <span class="btn btn-blue" style="left:132px;top:302px;width:118px;height:40px">Learn more</span>
  <span class="slider-arrow" style="left:0;top:210px"><svg width="14" height="20"><path d="M11 2 3 10l8 8" stroke="#fff" stroke-width="2.5" fill="none"/></svg></span>
  <span class="slider-arrow" style="left:1154px;top:210px"><svg width="14" height="20"><path d="m3 2 8 8-8 8" stroke="#fff" stroke-width="2.5" fill="none"/></svg></span>
</section>

<section class="intro">
  <span class="intro-rule" style="left:415px"></span>
  <span class="intro-rule" style="left:790px"></span>
  <span class="intro-icon" style="left:180px;background:var(--blue)"><svg width="44" height="44" viewBox="0 0 44 44" fill="none" stroke="#fff" stroke-width="2"><path d="M6 20a16 16 0 0 1 32 0z"/><path d="M22 20v16a3 3 0 0 1-6 0"/><circle cx="17" cy="28" r="3"/><circle cx="27" cy="28" r="3"/></svg></span>
  <span class="intro-icon" style="left:550px;background:var(--sky)"><svg width="44" height="44" viewBox="0 0 44 44" fill="#fff"><circle cx="15" cy="14" r="4"/><circle cx="29" cy="14" r="4"/><path d="M11 20h8v16h-8zM25 20h8l2 10h-4v6h-4v-6h-4z"/></svg></span>
  <span class="intro-icon" style="left:920px;background:var(--yellow)"><svg width="44" height="44" viewBox="0 0 44 44" fill="none" stroke="#555" stroke-width="1.6"><circle cx="22" cy="22" r="5"/><path d="M22 4v10M22 30v10M4 22h10M30 22h10M9 9l7 7M28 28l7 7M35 9l-7 7M16 28l-7 7"/></svg></span>
  <p class="intro-text" style="left:90px">Are you stuck in a rut or at a crossroads in life?</p>
  <p class="intro-text" style="left:460px">Do you have ongoing problems with your career, relationship or life?</p>
  <p class="intro-text" style="left:830px">Would you like to change direction, or gain a vision for your life?</p>
</section>

<section class="about">
  <h2 class="section-title heading abs" style="left:135px;top:48px">About us</h2>
  <div class="about-card">
    <p style="top:40px">Coaching is about establishing a partnership with you to create positive change. Through a process of self-awareness, strategic action and structured accountability, coaching leads you to reach your ultimate personal and/or professional potential. Unlike counseling, which focuses on the past to identify current struggles and obstacles, coaching starts with where you are now and focuses on where you want to next in your life.</p>
    <p style="top:236px">Coaching helps you regain clarity and creates a life changing course for your future. We use proven processes that help you overcome barriers and limiting beliefs.</p>
    <span class="btn btn-blue" style="left:53px;top:332px;width:118px;height:40px">Read more</span>
  </div>
  <div class="about-photo" role="img" aria-label="The two founding coaches standing together at an event backdrop"></div>
</section>

<section class="services">
  <h2 class="section-title heading abs" style="left:0;top:68px;width:1200px;text-align:center">Our services</h2>
  <span class="title-rule"></span>
  <svg class="abs" style="left:68px;top:322px" width="22" height="44"><path d="M19 2 3 22l16 20" stroke="#bbb" stroke-width="2" fill="none"/></svg>
  <svg class="abs" style="left:1110px;top:322px" width="22" height="44"><path d="m3 2 16 20L3 42" stroke="#bbb" stroke-width="2" fill="none"/></svg>
  <div class="service-card" style="left:133px;border-color:var(--sky)">
    <div class="photo" role="img" aria-label="Laughing couple sharing a hug" style="background:linear-gradient(160deg,#e9c7a4,#b97a55 60%,#8e5a3f)"></div>
    <h3>Relationships<br>and career</h3>
    <span class="btn" style="background:var(--sky);color:#fff;left:24px;top:252px;width:100px;height:30px;font-size:11px">Read more</span>
  </div>
  <div class="service-card" style="left:453px;border-color:var(--yellow)">
    <div class="photo" role="img" aria-label="Person with arms outstretched in a sunlit field" style="background:linear-gradient(180deg,#d8cf9d,#b6a66a 55%,#756738)"></div>
    <h3>Personal<br>development</h3>
    <span class="btn btn-yellow" style="left:24px;top:252px;width:100px;height:30px;font-size:11px">Read more</span>
  </div>
  <div class="service-card" style="left:771px;border-color:var(--blue)">
    <div class="photo" role="img" aria-label="Business team in a bright office meeting" style="background:linear-gradient(160deg,#e6ecf2,#a9b6c6 55%,#5c6b80)"></div>
    <h3>Professional<br>development</h3>
    <span class="btn btn-blue" style="left:24px;top:252px;width:100px;height:30px;font-size:11px">Read more</span>
  </div>
</section>

<section class="video">
  <div class="video-panel">
    <h2>Our video</h2>
    <p>Play<br>teachers<br>trust</p>
    <span class="btn btn-yellow" style="left:44px;top:292px;width:150px;height:44px;font-size:14px">Watch now</span>
  </div>
  <div class="video-frame" role="img" aria-label="Parent and child lying on the grass laughing together">
    <svg class="abs" style="left:300px;top:150px" width="84" height="58"><rect width="84" height="58" rx="4" fill="#1c4f91" opacity=".85"/><path d="M34 17v24l20-12z" fill="#fff"/></svg>
    <div class="video-bar">
      <svg class="abs" style="left:10px;top:18px" width="660" height="20">
        <path d="M2 2v12l10-6z" fill="#fff"/>
        <rect x="36" y="7" width="520" height="3" fill="#9aa"/>
        <rect x="36" y="7" width="70" height="3" fill="#2f8fe0"/>
        <circle cx="106" cy="8.5" r="5" fill="#fff"/>
        <text x="568" y="12" font-size="10" fill="#fff" font-family="Open Sans, sans-serif">-0:46</text>
        <circle cx="606" cy="8" r="5" fill="#fff"/>
        <rect x="622" y="3" width="10" height="10" fill="none" stroke="#fff" stroke-width="1.5"/>
        <path d="M642 5h3l4-3v12l-4-3h-3z" fill="#fff"/>
      </svg>
    </div>
    <span class="video-caption">Play teaches trust</span>
  </div>
</section>

<h2 class="call-title heading">Call now for a Free Coaching Consult!</h2>
<div class="contact-strip">
  <span class="contact-badge" style="left:20px"><svg width="18" height="18" viewBox="0 0 24 24"><path d="M6.6 10.8a15 15 0 0 0 6.6 6.6l2.2-2.2c.3-.3.7-.4 1-.2 1.1.4 2.3.6 3.6.6.6 0 1 .4 1 1V20c0 .6-.4 1-1 1A17 17 0 0 1 3 4c0-.6.4-1 1-1h3.5c.6 0 1 .4 1 1 0 1.3.2 2.5.6 3.6.1.3 0 .7-.2 1z" fill="#0d4ea6"/></svg></span>
  <div class="contact-item" style="left:80px"><small>Ashgrove</small><b>555-014-2200</b></div>
  <span class="contact-rule" style="left:250px"></span>
  <div class="contact-item" style="left:265px"><small>Kellan</small><b>555-016-4636</b></div>
  <span class="contact-rule" style="left:435px"></span>
  <div class="contact-item" style="left:452px"><small>Fairmoor</small><b>555-018-4636</b></div>
  <span class="contact-rule" style="left:630px;top:0;height:118px"></span>
  <span class="contact-badge" style="left:652px"><svg width="18" height="14" viewBox="0 0 18 14"><rect width="18" height="14" rx="1" fill="#0d4ea6"/><path d="M1 1l8 6 8-6" stroke="#fbe08a" stroke-width="1.5" fill="none"/></svg></span>
  <div class="contact-item" style="left:716px"><small>Email us</small><b style="font-size:18px">info@OrembyPathHouse.com</b></div>
</div>

<footer class="site-footer">
  <div class="footer-brand"><span class="brand-dot"></span><span class="brand-name">OREMBY<br>PATH HOUSE</span></div>
  <div class="footer-col" style="left:452px">
    <h4>Menu</h4>
    <ul><li>Home</li><li>About us</li><li>Services</li><li>Blog</li><li>Contact us</li></ul>
  </div>
  <div class="footer-col" style="left:592px">
    <h4>Follow us</h4>
    <div class="social"><span class="dot" style="background:#3b5ba0"></span>Like us on Friendwall</div>
    <div class="social"><span class="dot" style="background:#2aa3e0"></span>Follow us on Chirper</div>
    <div class="social"><span class="dot" style="background:#e2533a"></span>Follow us on Circlesphere</div>
  </div>
  <div class="footer-col" style="left:817px">
    <h4>Newsletter signup!</h4>
    <div class="newsletter-field"><svg width="12" height="9"><rect x=".5" y=".5" width="11" height="8" fill="none" stroke="#c7d7ee"/><path d="M1 1l5 4 5-4" stroke="#c7d7ee" fill="none"/></svg>E-mail id</div>
    <span class="btn" style="position:relative;display:flex;margin:14px 0 0 154px;width:96px;height:38px;background:var(--yellow-strong);color:var(--blue)">Signup!</span>
  </div>
  <span class="footer-rule"></span>
  <p class="copyright">Copyrights @ 2016 All Rights Reserved</p>
</footer>

</body>
</html>
```